Maplecrest Counseling and Consulting, LLC

We need a business card and stationary designed for a new therapy practice for Laura Whitcombe. Laura Whitcombe is a Therapist who specializes in Therapy for children dealing with trauma and/or stress. Below are some of her thoughts:
colors can include purple, blue, turquoise and green (does NOT have to be all colors) See attached Logos
Laura Whitcombe, LMHC
Maplecrest Counseling & Counseling Inc.
4382 W. Harbor Parkway
Suite 714
Alderbrook, ST 33912
Phone: 555-730-2254
Fax: 555-730-2255
Email: laura@maplecrestcc-example.com
Website: www.maplecrestcc-example.com

```html
<!DOCTYPE html>
<html lang="en">
<head>
<meta charset="utf-8">
<title>Maplecrest Counseling &amp; Consulting – Business Card</title>
<link rel="stylesheet" href="https://fonts.googleapis.com/css2?family=Source+Sans+3:wght@400;600;700&display=swap">
<style>
  :root {
    --backdrop: #ecebe8;
    --card: #ffffff;
    --plum: #4f1a5c;
    --plum-text: #5a2468;
    --mist: #e2e2e5;
    --mist-light: #f3f3f5;
    --info-grey: #a4a4aa;
    --white: #ffffff;
  }
  * { margin: 0; padding: 0; box-sizing: border-box; }
  html, body {
    width: 1200px; height: 675px; overflow: hidden;
    background: var(--backdrop);
    font-family: "Source Sans 3", "Myriad Pro", Arial, sans-serif;
  }
  .canvas { position: relative; width: 1200px; height: 675px; }
  .business-card {
    position: absolute; left: 180px; top: 97px;
    width: 840px; height: 480px;
    background: var(--card);
    overflow: hidden;
    box-shadow: 0 6px 24px rgba(0,0,0,0.12);
  }
  .brand-band {
    position: absolute; left: 0; top: 0; width: 100%; height: 104px;
    background: var(--plum);
  }
  .brand-name {
    position: absolute; top: 20px; width: 100%;
    text-align: center; color: var(--white);
    font-size: 36px; font-weight: 400; letter-spacing: 5px;
  }
  .brand-tagline {
    position: absolute; top: 68px; width: 100%;
    text-align: center; color: var(--white);
    font-size: 14px; letter-spacing: 0.5px; opacity: 0.85;
  }
  .mascot-area {
    position: absolute; left: 20px; top: 104px; width: 400px; height: 376px;
  }
  .practitioner {
    position: absolute; top: 190px; width: 100%;
    text-align: center; color: var(--plum-text);
    font-size: 32px; font-weight: 700;
  }
  .contact-lines {
    position: absolute; top: 290px; left: 60px; right: 40px;
    text-align: center; color: var(--info-grey);
    font-size: 18px; line-height: 1.7;
  }
  .contact-label { font-size: 14px; }
</style>
</head>
<body>
<div class="canvas">
  <div class="business-card">
    <div class="brand-band"></div>
    <svg class="mascot-area" viewBox="0 0 400 376" role="img" aria-label="Large faint elephant illustration">
      <defs>
        <radialGradient id="mascotTone" cx="50%" cy="40%" r="60%">
          <stop offset="0%" stop-color="var(--mist)"/>
          <stop offset="100%" stop-color="var(--mist-light)"/>
        </radialGradient>
      </defs>
      <rect x="0" y="0" width="400" height="376" rx="60" fill="url(#mascotTone)" opacity="0.6"/>
    </svg>
    <div class="brand-name">Maplecrest</div>
    <div class="brand-tagline">Counseling &amp; Consulting, Inc.</div>
    <div class="practitioner">Laura Whitcombe, LMHC</div>
    <div class="contact-lines">
      <p>4382 W. Harbor Parkway | Suite 714 | Alderbrook, ST 33912</p>
      <p><span class="contact-label">Phone:</span> 555-730-2254 | <span class="contact-label">Fax:</span> 555-730-2255</p>
      <p><span class="contact-label">Email:</span> laura@maplecrestcc-example.com | <span class="contact-label">Website:</span> www.maplecrestcc-example.com</p>
    </div>
  </div>
</div>
</body>
</html>
```